Brochure design for 3D ultrasound company

I am looking for a clean and modern and edgy brochure for my ultrasound company. We are a fairly new company specialize in 3D/4D ultrasounds.Our brochures will be placed in OB-GYN offices in high end areas around Los Angeles, so we need something that will stand out and capture a modern woman's attention. Our logo is currently in the process of being designed, so I don't have a picture to provide quite yet, however it will be our company name"Kite + Lantern" written in a special font that looks like neon lights. I will attach a few images of what our logo will be like, and some initial content that can help provide the layout we would like for the brochure. please feel free to also take a look at our website. www.kitelanternscan.example.

Target Market(s)

Upscale trendy women.

Colors
eea4c8
33a6d7
fee18a

Requirements
Should not have
• too many colors.

```html
<!DOCTYPE html>
<html lang="en">
<head>
<meta charset="utf-8">
<title>Kite + Lantern – Services + Pricing Brochure</title>
<link href="https://fonts.googleapis.com/css2?family=Cabin:ital,wght@0,400;0,500;0,600;0,700;1,600;1,700&display=swap" rel="stylesheet">
<style>
  :root{
    --pink:#e9818f;
    --pink-soft:#f2b3bc;
    --cocoa:#3a2d2e;
    --cocoa-deep:#2b2122;
    --ink:#2a2223;
    --paper:#ffffff;
    --canvas-bg:#e6e6e6;
    --smoke-dark:#2f3a2c;
    --smoke-pink:#d9707f;
    --skin:#e9d3c6;
  }
  *{box-sizing:border-box;margin:0;padding:0}
  html,body{width:1200px;height:847px;overflow:hidden;background:var(--canvas-bg)}
  body{font-family:"Cabin",sans-serif;color:var(--ink)}
  .brochure{position:relative;width:1200px;height:847px;background:var(--paper);overflow:hidden}

  /* top row */
  .hero-photo{position:absolute;left:0;top:0;width:800px;height:400px;
    background:radial-gradient(ellipse at 42% 55%,var(--smoke-pink) 0%,#b45d6c 22%,#6a3f45 45%,var(--smoke-dark) 78%);}
  .contact-panel{position:absolute;left:800px;top:0;width:400px;height:400px;background:var(--cocoa)}
  .fold{position:absolute;top:0;width:1px;height:847px;background:rgba(0,0,0,.08)}

  .popular{position:absolute;left:40px;top:36px;color:var(--paper);text-transform:uppercase;line-height:1}
  .popular small{display:block;font-size:17px;font-weight:500;letter-spacing:1px}
  .popular strong{display:block;font-size:30px;font-weight:600;letter-spacing:1px;margin-top:4px}

  .package{position:absolute}
  .package h3{color:var(--pink);font-weight:600;text-transform:uppercase;letter-spacing:.5px}
  .package ul{list-style:none}
  .package li{font-weight:600;line-height:1.22}
  .package li::before{content:"•";margin-right:8px}

  .reveal{left:470px;top:150px;color:var(--paper)}
  .reveal h3{font-size:16px}
  .reveal ul{margin-top:10px;margin-left:40px;font-size:16px;width:190px}
  .reveal li{color:var(--paper)}

  .price{position:absolute;background:var(--cocoa-deep);color:var(--paper);font-size:22px;font-weight:500;
    padding:6px 14px;border-radius:6px;white-space:nowrap}
  .price sup{font-size:11px;vertical-align:top;position:relative;top:2px;margin-right:1px}
  .price::before{content:"";position:absolute;left:10px;top:-12px;border-left:0 solid transparent;
    border-right:14px solid transparent;border-bottom:13px solid var(--cocoa-deep)}
  .price.pink{background:var(--pink)}
  .price.pink::before{top:auto;bottom:-12px;border-bottom:0;border-top:13px solid var(--pink)}

  .contact-panel h2{position:absolute;left:40px;top:70px;font-size:27px;font-style:italic;font-weight:700;
    color:#f1e6e4;line-height:1.15;width:320px}
  .contact-panel .lead{position:absolute;left:40px;font-size:14px;color:var(--pink)}
  .contact-line{position:absolute;left:40px;display:flex;align-items:center;gap:10px;color:var(--pink)}
  .contact-line.phone{top:210px;font-size:27px;font-weight:600}
  .contact-line.web{top:290px;font-size:18px;font-weight:500}

  /* band */
  .band{position:absolute;left:0;top:400px;width:1200px;height:62px;background:var(--pink);color:var(--paper)}
  .band .title{position:absolute;left:40px;top:13px;font-size:30px;letter-spacing:1px;text-transform:uppercase}
  .band .note{position:absolute;left:430px;top:8px;width:740px;font-size:19px;font-weight:600;line-height:1.2}

  /* bottom row */
  .scene{position:absolute;top:462px;width:400px;height:385px}
  .scene-left{left:0;background:linear-gradient(180deg,#e7cbbd 0%,#f0ddd3 45%,#fff 85%)}
  .scene-mid{left:400px;background:linear-gradient(180deg,#efd9cc 0%,#f5e8e1 45%,#fff 85%)}
  .scene-right{left:800px;background:linear-gradient(180deg,#d9c3b4 0%,#ece0d8 45%,#fff 85%)}

  .peek{left:40px;top:640px}
  .momma{left:440px;top:640px}
  .vib{left:830px;top:640px}
  .bottom-list{font-size:16px;margin-bottom:14px}
  .bottom-list li{color:var(--ink)}
  .bottom-title{font-size:25px}
  .bottom-title span{font-size:14px}
  .peek .price,.momma .price,.vib .price{position:relative;display:inline-block;margin-top:20px}
</style>
</head>
<body>
<main class="brochure">
  <div class="hero-photo" role="img" aria-label="Photo: expectant mother in white covering her eyes amid pink smoke, greenery behind"></div>
  <section class="contact-panel">
    <h2>Ready for your baby’s first photoshoot?</h2>
    <p class="lead" style="top:170px">Give us a call to schedule an appointment</p>
    <p class="contact-line phone">
      <svg width="26" height="26" viewBox="0 0 24 24" aria-hidden="true"><path fill="#f1e6e4" d="M6.6 10.8a15 15 0 006.6 6.6l2.2-2.2a1 1 0 011-.25 11.4 11.4 0 003.6.57 1 1 0 011 1V20a1 1 0 01-1 1A17 17 0 013 4a1 1 0 011-1h3.5a1 1 0 011 1 11.4 11.4 0 00.57 3.6 1 1 0 01-.25 1z"/></svg>
      (555) 014-2290
    </p>
    <p class="lead" style="top:262px">or visit our website</p>
    <p class="contact-line web">
      <svg width="24" height="24" viewBox="0 0 24 24" aria-hidden="true" fill="none" stroke="#f1e6e4" stroke-width="1.4"><circle cx="12" cy="12" r="9"/><ellipse cx="12" cy="12" rx="4" ry="9"/><path d="M3 12h18M5 7h14M5 17h14"/></svg>
      kitelanternscan.example
    </p>
  </section>

  <div class="popular"><small>Our most</small><strong>Popular package</strong></div>

  <section class="package reveal">
    <h3>The Big Reveal!!</h3>
    <ul>
      <li>25 minute 3D/4D/HD live session</li>
      <li>5 black and white pictures</li>
      <li>5 color pictures</li>
      <li>Email or USB flash drive with all images</li>
      <li>Record and hear heartbeat</li>
      <li>Confirm gender</li>
    </ul>
    <span class="price pink" style="left:170px;top:-8px"><sup>$</sup>225.00</span>
  </section>

  <div class="band">
    <span class="title">Services + Pricing</span>
    <p class="note">We are available for private in-home screenings, gender reveals, baby showers, or any other special occasion!</p>
  </div>

  <div class="scene scene-left" role="img" aria-label="Photo: hands holding an ultrasound print in front of a pregnant belly"></div>
  <div class="scene scene-mid" role="img" aria-label="Photo: pregnant belly with a plush bunny toy resting on it"></div>
  <div class="scene scene-right" role="img" aria-label="Photo: couple holding boy and girl cards"></div>

  <section class="package peek">
    <ul class="bottom-list">
      <li>5 minute 2D session</li>
      <li>3 black and white images</li>
      <li>Listen to baby’s heartbeat</li>
      <li>Confirm gender</li>
    </ul>
    <h3 class="bottom-title">Peek-a-boo</h3>
    <span class="price"><sup>$</sup>125.00</span>
  </section>

  <section class="package momma">
    <ul class="bottom-list">
      <li>15 minute 3D/4D/HD live session</li>
      <li>3 black and white images</li>
      <li>2 color images</li>
      <li>Listen to baby’s heartbeat</li>
      <li>Confirm gender</li>
    </ul>
    <h3 class="bottom-title">Hello, Momma</h3>
    <span class="price"><sup>$</sup>165.00</span>
  </section>

  <section class="package vib">
    <ul class="bottom-list">
      <li>30 min 3D/4D/HD live session on our projector</li>
      <li>10 color images</li>
      <li>Email or USB with all images</li>
      <li>Record and hear heartbeat</li>
      <li>Confirm gender</li>
    </ul>
    <h3 class="bottom-title">V.I.B <span>(Very important baby)</span></h3>
    <span class="price"><sup>$</sup>325.00</span>
  </section>

  <div class="fold" style="left:400px"></div>
  <div class="fold" style="left:800px"></div>
</main>
</body>
</html>
```